Zielgruppe
Wir sind eine Wäscherei.
Zielgruppe: Kunden aus der Hotel- und Gastronomiebranche
Aufgabenstellung
Wir benötigen einen 2-seitigen Flyer DIN lang. 9,8 x21cm
TextInhalte sind in der Vorlage-Datei.
Bilder sind eingefügt.

```html
<!DOCTYPE html>
<html lang="de">
<head>
<meta charset="utf-8">
<title>Waschhaus Brendel – Flyer</title>
<link rel="stylesheet" href="https://fonts.googleapis.com/css2?family=Mulish:wght@400;700;800&display=swap">
<style>
  :root {
    --magenta: #c4007a;
    --ink: #1d1d1b;
    --paper: #ffffff;
    --linen-light: #f6f3f1;
    --linen-mid: #ddd6d2;
    --linen-dark: #b9b0aa;
    --leaf: #7d9a4a;
  }
  * { margin: 0; padding: 0; box-sizing: border-box; }
  html, body { width: 1200px; height: 560px; overflow: hidden; background: var(--paper); }
  body { font-family: "Mulish", sans-serif; color: var(--ink); }

  .flyer { position: relative; width: 1200px; height: 560px; overflow: hidden; background: var(--paper); }

  .brand-name {
    position: absolute; left: 57px; top: 146px;
    font-family: "Mulish", sans-serif; font-weight: 800;
    font-size: 40px; letter-spacing: 0.5px; text-transform: uppercase;
    color: var(--magenta);
  }

  .services { position: absolute; left: 57px; top: 248px; }
  .services__headline {
    font-weight: 700; font-size: 17.5px; color: var(--magenta);
    margin-bottom: 3px;
  }
  .services__list { list-style: none; }
  .services__item {
    font-size: 17.5px; line-height: 24px; position: relative; padding-left: 11px;
  }
  .services__item::before {
    content: ""; position: absolute; left: 0; top: 10px;
    width: 5px; height: 5px; background: var(--magenta); transform: rotate(45deg);
  }

  .contact {
    position: absolute; left: 57px; top: 491px;
    display: flex; align-items: center; gap: 4px;
    font-size: 11.5px; white-space: nowrap;
  }
  .contact__sep { width: 4px; height: 4px; background: var(--magenta); transform: rotate(45deg); margin: 0 2px; }
  .contact__icon { width: 11px; height: 11px; margin: 0 2px 0 8px; }

  .visual { position: absolute; inset: 0; pointer-events: none; }
</style>
</head>
<body>
<main class="flyer">
  <div class="brand-name">Waschhaus Brendel</div>

  <section class="services">
    <h2 class="services__headline">Serviettenfaltservice – ab November 2017</h2>
    <ul class="services__list">
      <li class="services__item">Hotel- und Gastronomiewäsche</li>
      <li class="services__item">Schmutzmatten</li>
      <li class="services__item">Gardinenservice</li>
      <li class="services__item">Berufskleidung</li>
      <li class="services__item">Private Wäsche</li>
      <li class="services__item">Verkauf von Hotel- und Gastronomietextilien</li>
    </ul>
  </section>

  <footer class="contact">
    <span>Waschhaus Brendel</span><span class="contact__sep"></span>
    <span>Lindenweg 12</span><span class="contact__sep"></span>
    <span>71000 Talheim</span>
    <svg class="contact__icon" viewBox="0 0 24 24" aria-hidden="true"><path fill="var(--magenta)" d="M6.6 10.8a15.1 15.1 0 0 0 6.6 6.6l2.2-2.2a1 1 0 0 1 1-.25 11.4 11.4 0 0 0 3.6.57 1 1 0 0 1 1 1V20a1 1 0 0 1-1 1A17 17 0 0 1 3 4a1 1 0 0 1 1-1h3.5a1 1 0 0 1 1 1c0 1.25.2 2.45.57 3.57a1 1 0 0 1-.25 1z"/></svg>
    <span>+49 (0) 7100 / 12 34 56</span>
    <svg class="contact__icon" viewBox="0 0 24 24" aria-hidden="true"><rect x="2" y="5" width="20" height="14" fill="none" stroke="var(--magenta)" stroke-width="2.4"/><path d="M2 5l10 8 10-8" fill="none" stroke="var(--magenta)" stroke-width="2.4"/></svg>
    <span>info@waschhaus-brendel.de</span>
  </footer>

  <svg class="visual" width="1200" height="560" viewBox="0 0 1200 560">
    <defs>
      <linearGradient id="table-tones" x1="0" y1="0" x2="0.6" y2="1">
        <stop offset="0" stop-color="var(--linen-dark)"/>
        <stop offset="0.35" stop-color="var(--linen-mid)"/>
        <stop offset="0.6" stop-color="var(--linen-light)"/>
        <stop offset="1" stop-color="#fbfaf9"/>
      </linearGradient>
      <radialGradient id="bouquet-tone" cx="0.75" cy="0.55" r="0.3">
        <stop offset="0" stop-color="var(--leaf)" stop-opacity="0.45"/>
        <stop offset="1" stop-color="var(--leaf)" stop-opacity="0"/>
      </radialGradient>
    </defs>
    <circle class="visual__ring" cx="985" cy="290" r="318" fill="var(--magenta)"/>
    <g role="img" aria-label="Foto: festlich eingedeckte Tafel mit weißen Tischdecken, gefalteten Servietten, Gläsern und Blumengesteck">
      <circle cx="1010" cy="290" r="308" fill="url(#table-tones)"/>
      <circle cx="1010" cy="290" r="308" fill="url(#bouquet-tone)"/>
    </g>
  </svg>
</main>
</body>
</html>
```